Newsletter Landing Page Design

It's a landing page for a newsletter. Add the form on the landing page.

The landing page aims to drive conversions by encouraging visitors to sign up for the Betting Newsletter. It should convey the value proposition clearly and effectively to attract sports enthusiasts and avid bettors. The design should create a sense of trust, showcase the benefits of subscribing, and guide visitors towards the sign-up process with a user-friendly and visually appealing layout.

Key Elements and Considerations:
The landing page should feature a clean and modern design, utilizing minimalistic aesthetics and intuitive navigation to ensure a seamless user experience. The layout should prominently highlight the unique selling points of the Betting Newsletter, such as expert insights, valuable tips, exclusive promotions, and breaking news updates. Compelling imagery that resonates with the target audience should be incorporated to evoke excitement and credibility. The page should have a responsive design that adapts to different devices and screen sizes, making it accessible to users across platforms. Additionally, trust elements such as testimonials or affiliations with respected experts or organizations should be included to instill confidence. The sign-up process should be user-friendly, capturing essential information without overwhelming visitors. Privacy and data security should be emphasized, and analytics and tracking tools should be implemented for optimization purposes.

By incorporating these elements, the landing page will effectively communicate the value of the Betting Newsletter, provide a seamless user experience, and drive conversions by encouraging visitors to sign up.

Target Market(s)

People looking for Gambling information

Industry/Entity Type

Gambling

Number of Pages Required

1 page

Font styles to use
Sans Serif

Requirements
Must have
• Clean design, modern looking, not elementor looking
Nice to have
• Bold ideas, engaging, and features a human element

```html
<!DOCTYPE html>
<html lang="en">
<head>
<meta charset="UTF-8">
<title>Betting Newsletter</title>
<link href="https://fonts.googleapis.com/css2?family=Poppins:wght@600;700&family=Nunito+Sans:wght@600&display=swap" rel="stylesheet">
<style>
  :root {
    --bg-deep: #010717;
    --bg-navy: #03102a;
    --ring: #0d2c3e;
    --ring-inner: #0f3346;
    --portrait-dark: #02041a;
    --portrait-light: #6f7680;
    --heading: #ffffff;
    --lead: #1a6b87;
    --cta: #29d6f7;
    --cta-text: #0f2233;
  }
  * { margin: 0; padding: 0; box-sizing: border-box; }
  html, body { width: 1200px; height: 675px; overflow: hidden; }
  body {
    background: radial-gradient(ellipse at 70% 40%, var(--bg-navy), var(--bg-deep) 70%);
    font-family: "Poppins", sans-serif;
    position: relative;
  }
  .hero-rings {
    position: absolute;
    left: 0; top: 0;
    width: 1200px; height: 675px;
  }
  .hero-copy {
    position: absolute;
    left: 94px;
    top: 178px;
    z-index: 2;
  }
  .hero-title {
    color: var(--heading);
    font-weight: 700;
    font-size: 67px;
    line-height: 83px;
    letter-spacing: -0.5px;
  }
  .hero-lead {
    margin-top: 20px;
    margin-left: 6px;
    color: var(--lead);
    font-family: "Nunito Sans", sans-serif;
    font-weight: 600;
    font-size: 18px;
    line-height: 25px;
    letter-spacing: 1.3px;
  }
  .cta-button {
    display: flex;
    align-items: center;
    justify-content: center;
    margin-top: 26px;
    margin-left: 6px;
    width: 255px;
    height: 52px;
    border-radius: 26px;
    background: var(--cta);
    color: var(--cta-text);
    font-weight: 700;
    font-size: 19px;
    letter-spacing: 1.2px;
    text-decoration: none;
  }
</style>
</head>
<body>
  <svg class="hero-rings" viewBox="0 0 1200 675" aria-hidden="false">
    <defs>
      <linearGradient id="portraitTone" x1="0" y1="0" x2="1" y2="1">
        <stop offset="0" stop-color="var(--portrait-dark)"/>
        <stop offset="0.55" stop-color="#3a3f48"/>
        <stop offset="1" stop-color="var(--portrait-light)"/>
      </linearGradient>
    </defs>
    <circle cx="869" cy="339" r="271" fill="none" stroke="var(--ring)" stroke-width="38"/>
    <circle cx="869" cy="339" r="206" fill="none" stroke="var(--ring-inner)" stroke-width="28"/>
    <circle cx="869" cy="339" r="192" fill="url(#portraitTone)" role="img" aria-label="Portrait photo of a smiling man giving a thumbs up"/>
  </svg>

  <main class="hero-copy">
    <h1 class="hero-title">Join the best<br>betting newsletter</h1>
    <p class="hero-lead">Lorem ipsum dolor sit amet, consectetur<br>adipisicing elit, sed do eiusmod.</p>
    <a class="cta-button" href="#subscribe">SUBSCRIBE NOW</a>
  </main>
</body>
</html>
```